Letterhead

We have a new logo and would like to design electronic letterhead with our new logo. We have two office locations. One of our offices is moving in July.

```html
<!DOCTYPE html>
<html lang="en">
<head>
<meta charset="utf-8">
<title>Meriden Law Letterhead</title>
<link rel="stylesheet" href="https://fonts.googleapis.com/css2?family=Open+Sans:wght@400&family=Roboto:wght@400&display=swap">
<style>
  :root {
    --backdrop: #dcdcdc;
    --paper: #f9f9f9;
    --navy: #2c3049;
    --blue: #3d7fc0;
    --body-text: #5a5a5a;
    --footer-text: #4a4a4a;
    --signature-tone: #e6e6e8;
  }
  * { box-sizing: border-box; margin: 0; padding: 0; }
  html, body {
    width: 1200px; height: 800px; overflow: hidden;
    background: var(--backdrop);
  }
  .letterhead {
    position: absolute; left: 328px; top: 20px;
    width: 544px; height: 760px;
    background: var(--paper);
    font-family: "Open Sans", sans-serif;
    color: var(--body-text);
  }
  .brand {
    position: absolute; top: 68px; left: 0; right: 0;
    text-align: center;
    font-family: "Open Sans", sans-serif;
    font-weight: 400;
    font-size: 40px;
    letter-spacing: 1px;
    color: var(--navy);
    line-height: 1;
  }
  .letter-body {
    position: absolute; left: 49px; right: 55px; top: 168px;
    font-size: 10px; line-height: 14.8px;
  }
  .letter-body p { margin-bottom: 14.6px; text-align: justify; }
  .letter-body .salutation, .letter-body .closing { text-align: left; }
  .signature {
    position: absolute; left: 49px; top: 556px;
    width: 64px; height: 60px;
    background: var(--signature-tone);
  }
  .contact-bar {
    position: absolute; left: 49px; right: 55px; top: 700px;
    display: flex; justify-content: space-between; gap: 8px;
    font-family: "Roboto", sans-serif;
    font-size: 10.5px; line-height: 14px;
    color: var(--footer-text);
    white-space: nowrap;
  }
  .contact-item { display: flex; align-items: center; gap: 4px; }
  .contact-item svg { width: 9px; height: 9px; fill: var(--blue); flex: none; }
  .accent-band {
    position: absolute; left: 0; bottom: 0;
    width: 544px; height: 10px; display: block;
  }
</style>
</head>
<body>
<main class="letterhead">
  <div class="brand">MERIDEN LAW</div>

  <section class="letter-body">
    <p class="salutation">Dear customer,</p>
    <p>Lorem ipsum dolor sit amet, consectetur adipisicing elit, sed do eiusmod tempor incididunt ut labore et dolore magna aliqua. Ut enim ad minim veniam, quis nostrud exercitation ullamco laboris nisi ut aliquip ex ea commodo consequat. Duis aute irure dolor in reprehenderit in voluptate velit esse cillum dolore eu fugiat nulla pariatur. Excepteur sint occaecat cupidatat non proident, sunt in culpa qui officia deserunt mollit anim id est laborum.</p>
    <p>Lorem ipsum dolor sit amet, consectetur adipisicing elit, sed do eiusmod tempor incididunt ut labore et dolore magna aliqua. Ut enim ad minim veniam, quis nostrud exercitation ullamco laboris nisi ut aliquip ex ea commodo consequat. Duis aute irure dolor in reprehenderit in voluptate velit esse cillum dolore eu fugiat nulla pariatur. Excepteur sint occaecat cupidatat non proident, sunt in culpa qui officia deserunt mollit anim id est laborum.</p>
    <p>Lorem ipsum dolor sit amet, consectetur adipisicing elit, sed do eiusmod tempor incididunt ut labore et dolore magna aliqua. Ut enim ad minim veniam, quis nostrud exercitation ullamco laboris nisi ut aliquip ex ea commodo consequat. Duis aute irure dolor in reprehenderit in voluptate velit esse cillum dolore eu fugiat nulla pariatur. Excepteur sint occaecat cupidatat non proident, sunt in culpa qui officia deserunt mollit anim id est laborum.</p>
    <p>Lorem ipsum dolor sit amet, consectetur adipisicing elit, sed do eiusmod tempor incididunt ut labore et dolore magna aliqua. Ut enim ad minim veniam, quis nostrud exercitation ullamco laboris nisi ut aliquip ex ea commodo consequat. Duis aute irure dolor in reprehenderit.</p>
    <p class="closing">Yours Sincerely,</p>
  </section>

  <div class="signature" role="img" aria-label="Handwritten signature of the sender"></div>

  <footer class="contact-bar">
    <div class="office">418 Harbor Ave., Ste 210<br>Ashford, WA 98410 USA</div>
    <div class="phones">
      <div class="contact-item">
        <svg viewBox="0 0 10 10"><path d="M1 3.5C1 2 3 1 5 1s4 1 4 2.5L7.5 4.5 6.8 3.2H3.2L2.5 4.5ZM2.5 5h5L8.5 9h-7Z"/></svg>
        <span>(555) 014-2286</span>
      </div>
      <div class="contact-item">
        <svg viewBox="0 0 10 10"><path d="M3 1h4v2H3ZM1 3.5h8V8H7.5V6h-5v2H1ZM3 6.8h4V9H3Z"/></svg>
        <span>(555) 014-7731</span>
      </div>
    </div>
    <div class="online">
      <div class="contact-item">
        <svg viewBox="0 0 10 10"><path d="M1 2.5h8v5H1Z M1 2.5l4 3 4-3" fill="none" stroke="#3d7fc0" stroke-width="1"/></svg>
        <span>info@meriden.law</span>
      </div>
      <div class="contact-item">
        <svg viewBox="0 0 10 10"><circle cx="5" cy="5" r="4" fill="none" stroke="#3d7fc0" stroke-width="1.2"/><path d="M3 3h3l-1 2h2l-2 3-1-2H3Z"/></svg>
        <span>www.meriden.law</span>
      </div>
    </div>
    <div class="office">610 Cedar Row 500<br>Kenmore, WA 98120</div>
  </footer>

  <svg class="accent-band" viewBox="0 0 544 10" preserveAspectRatio="none" aria-hidden="true">
    <polygon points="0,0 270,0 275,10 0,10" fill="var(--navy)"/>
    <polygon points="273,0 544,0 544,10 278,10" fill="var(--blue)"/>
  </svg>
</main>
</body>
</html>
```